Beautiful Quotes For Social Media Posts

We are looking for 5 beautifully designed quotes for our social media account.

Inspiration of styles we like in both style and color along with a few of our favorite fonts (you are NOT limited to these fonts this is just to give you an idea):
https://quillmorestudio.example.com/s/k7p2vx9tqa41mzn8wbd3ce6hr5lf0y2j

*These fonts are property of Quillmore Studio. You do not have permission/rights to use them outside of this assignment*

Quotes to use (5):
“Only those who dare to fail greatly can ever achieve greatly.” –Vernon T. Ashgrove
“Don’t go through life, grow through life.” – Milo Pendrake
“Follow your bliss and the universe will open doors where there were only walls.” – Arthur Venholm
“If you don’t like the road you’re walking, start paving another one.” – Greta Mossley
“Life is like riding a bicycle. To keep your balance, you must keep moving.” —Lucian Thornwick

File Specifics:
- JPG
- 10x10 in size (square)
- Please include @QuillmoreStudio in the bottom right left or center of each design

Brand Details:
Soft but rich pastel and bright colors.
Hand Drawn florals, doodles and art
Handwritten looking fonts
Artsy, Creative, Girl and Inspiring

```html
<!DOCTYPE html>
<html lang="en">
<head>
<meta charset="utf-8">
<title>Quote Post – Fail Greatly</title>
<link rel="stylesheet" href="https://fonts.googleapis.com/css2?family=Caveat+Brush&family=Gochi+Hand&family=Tinos&display=swap">
<style>
  :root {
    --teal: #4cbfc0;
    --teal-deep: #3aa9aa;
    --white: #ffffff;
    --shadow: rgba(20, 70, 72, 0.35);
    --leaf-fill: rgba(255, 255, 255, 0.28);
  }
  * { margin: 0; padding: 0; box-sizing: border-box; }
  html, body {
    width: 1200px;
    height: 1200px;
    overflow: hidden;
    background: var(--teal);
  }
  .post {
    position: relative;
    width: 1200px;
    height: 1200px;
    background: radial-gradient(circle at 50% 45%, #52c4c5 0%, var(--teal) 60%, #47babb 100%);
    color: var(--white);
  }
  .frame {
    position: absolute;
    left: 61px;
    top: 61px;
    width: 1082px;
    height: 1082px;
    border: 4px solid var(--white);
  }
  .quote-line {
    position: absolute;
    left: 0;
    width: 100%;
    text-align: center;
    white-space: nowrap;
    text-shadow: 6px 8px 10px var(--shadow);
  }
  .quote-lead {
    top: 250px;
    font-family: "Gochi Hand", cursive;
    font-size: 50px;
    letter-spacing: 3px;
  }
  .quote-main {
    font-family: "Caveat Brush", cursive;
    font-size: 150px;
    line-height: 1;
  }
  .line-1 { top: 322px; }
  .line-2 { top: 436px; }
  .line-3 { top: 551px; }
  .line-4 { top: 666px; }
  .attribution {
    position: absolute;
    top: 890px;
    left: 0;
    width: 100%;
    text-align: center;
    font-family: "Tinos", serif;
    font-size: 35px;
    text-shadow: 3px 4px 6px var(--shadow);
  }
  .sprig {
    position: absolute;
    width: 155px;
    height: 230px;
    border-radius: 50% 50% 45% 45%;
    background: var(--leaf-fill);
  }
  .sprig-left { left: 222px; top: 422px; }
  .sprig-right { left: 822px; top: 422px; }
  .handle {
    position: absolute;
    right: 72px;
    top: 1114px;
    padding: 0 18px;
    background: var(--teal);
    font-family: "Caveat Brush", cursive;
    font-size: 44px;
    line-height: 56px;
    color: var(--white);
  }
</style>
</head>
<body>
  <main class="post">
    <div class="frame"></div>

    <div class="sprig sprig-left" role="img" aria-label="Hand-drawn white leafy sprig ornament"></div>
    <div class="sprig sprig-right" role="img" aria-label="Hand-drawn white leafy sprig ornament"></div>

    <p class="quote-line quote-lead">Only those who dare to</p>
    <p class="quote-line quote-main line-1">Fail Greatly</p>
    <p class="quote-line quote-main line-2">Can ever</p>
    <p class="quote-line quote-main line-3">Achieve</p>
    <p class="quote-line quote-main line-4">Greatly.</p>

    <p class="attribution">- Vernon T. Ashgrove -</p>

    <p class="handle">@QuillmoreStudio</p>
  </main>
</body>
</html>
```